Signage setout with photos for side of Mowing Trailer

We need signage for our mowing trailer to attract new business.
Specifically a Rear sign 1470x880mm and Side signs 2400x880mm
Sign needs to be modern and professional.
Some example uploads as to what we have thought about so far.
Logo doesn't need to be the green colour.
Logo words and Logo of Mower do not need to be together.
Link to get a mower image>
https://bluefernmachinery.com/torvo
Updates

Need extra days to review

Target Market(s)

Other Customers driving past the trailer.

Industry/Entity Type

Lawnmowing / Landscaping

Requirements
Must have
• Phone Number, Company Name & Logo, Web address, Linkup and Insta Logos, Comment - "Acreage & Commercial Specialists" Catchcry - "100% Electric Mowing Company - est 2017" Services "Mowing, Hedging, Pressure Cleaning, Weed Control, Fencing, Turfing, Mulching and Rubbish Removal"
Nice to have
• Full colour background images.

```html
<!DOCTYPE html>
<html lang="en">
<head>
<meta charset="utf-8">
<title>Bright Meadow Mowing – Trailer Signage</title>
<link rel="stylesheet" href="https://fonts.googleapis.com/css2?family=Ubuntu:wght@500;700&family=Arimo:wght@700&display=swap">
<style>
  :root {
    --page: #ffffff;
    --grass-light: #8fc442;
    --grass-mid: #74ad33;
    --grass-dark: #5a9426;
    --ink-green: #2a5e2c;
    --white: #ffffff;
    --accent-orange: #e8682a;
    --rider-tone: #3f6f2a;
    --rider-deep: #2f2f2f;
    --social-a: #3b5a9a;
    --social-b: #b13a8a;
  }
  * { margin: 0; padding: 0; box-sizing: border-box; }
  html, body { width: 1200px; height: 900px; overflow: hidden; background: var(--page); }
  .canvas { position: relative; width: 1200px; height: 900px; }

  .sign { position: absolute; overflow: hidden; }
  .sign--rear { left: 161px; top: 97px; width: 540px; height: 323px; }
  .sign--side { left: 163px; top: 485px; width: 882px; height: 323px; }

  .lawn-photo {
    position: absolute; inset: 0;
    background:
      radial-gradient(ellipse at 55% 45%, var(--grass-light) 0%, transparent 70%),
      linear-gradient(180deg, var(--grass-mid) 0%, var(--grass-light) 55%, var(--grass-dark) 100%);
  }
  .rider-photo {
    position: absolute;
    left: 196px; top: 84px; width: 110px; height: 104px;
    border-radius: 6px;
    background: linear-gradient(160deg, var(--rider-deep) 0%, var(--rider-tone) 45%, #6ccf3a 100%);
    opacity: .85;
  }

  .outlined {
    color: var(--white);
    text-shadow:
      -1.5px -1.5px 0 var(--ink-green), 1.5px -1.5px 0 var(--ink-green),
      -1.5px 1.5px 0 var(--ink-green), 1.5px 1.5px 0 var(--ink-green),
      0 0 3px var(--ink-green);
  }
  .haloed {
    color: var(--ink-green);
    text-shadow:
      -1.5px -1.5px 0 var(--white), 1.5px -1.5px 0 var(--white),
      -1.5px 1.5px 0 var(--white), 1.5px 1.5px 0 var(--white),
      0 0 6px var(--white);
  }

  .display { position: absolute; white-space: nowrap; line-height: 1; font-family: "Ubuntu", sans-serif; font-weight: 500; }
  .display--bold { font-weight: 700; }
  .services, .web { position: absolute; white-space: nowrap; line-height: 1; font-family: "Arimo", sans-serif; font-weight: 700; }
  .centered { text-align: center; }

  .brand {
    position: absolute; white-space: nowrap;
    font-family: "Ubuntu", sans-serif; font-weight: 700;
    color: var(--ink-green);
    text-align: center; line-height: 1.2;
  }
  .brand-dot { position: absolute; border-radius: 50%; background: var(--accent-orange); }

  .phone-icon { position: absolute; }
  .social {
    position: absolute; display: flex; flex-direction: column; align-items: center; gap: 2px;
    font-family: "Ubuntu", sans-serif; font-weight: 700; color: var(--white); line-height: 1;
  }
  .social-box { border-radius: 5px; display: block; }

  /* rear sign */
  .rear-brand { left: 20px; top: 96px; width: 170px; font-size: 20px; }
  .rear-est { left: 20px; top: 152px; width: 170px; font-size: 17px; }
  .rear-headline { left: 210px; width: 322px; font-size: 27px; }
  .rear-phone { left: 357px; top: 96px; font-size: 33px; }
  .rear-web { left: 311px; top: 134px; font-size: 12px; }
  .rear-tagline { left: 16px; top: 195px; font-size: 34px; }
  .rear-services { left: 0; width: 540px; font-size: 17px; }

  /* side sign */
  .side-brand { left: 0; top: 120px; width: 256px; font-size: 26px; }
  .side-headline { left: 259px; top: 21px; font-size: 39px; }
  .side-phone { left: 377px; top: 96px; font-size: 60px; }
  .side-web { left: 344px; top: 169px; font-size: 25px; }
  .side-tagline { left: 18px; top: 216px; font-size: 47px; }
  .side-est { left: 718px; top: 228px; font-size: 32px; }
  .side-services { left: 0; width: 882px; top: 290px; font-size: 17px; }
</style>
</head>
<body>
<main class="canvas">

  <section class="sign sign--rear" aria-label="Rear trailer sign">
    <div class="lawn-photo" role="img" aria-label="Photo of a freshly striped green lawn"></div>
    <div class="rider-photo" role="img" aria-label="Photo of an operator driving a Bluefern Torvo electric zero-turn mower"></div>

    <span class="brand-dot" style="left:78px;top:26px;width:52px;height:52px;"></span>
    <div class="brand rear-brand">BRIGHT MEADOW<br>MOWING</div>
    <div class="display haloed centered rear-est">- est 2017 -</div>

    <div class="display outlined centered rear-headline" style="top:12px;">Acreage &amp; Commercial</div>
    <div class="display outlined centered rear-headline" style="top:48px;">Specialists</div>

    <svg class="phone-icon" style="left:320px;top:97px;" width="28" height="28" viewBox="0 0 40 40" aria-hidden="true">
      <rect x="1" y="1" width="38" height="38" rx="9" fill="var(--ink-green)" stroke="var(--white)" stroke-width="2"/>
      <path d="M13 9c1.5-1 3-.5 3.5.8l2 4.5c.4 1-.1 2-1 2.6l-1.6 1c1.2 2.6 3.3 4.7 5.9 5.9l1-1.6c.6-.9 1.6-1.4 2.6-1l4.5 2c1.3.5 1.8 2 .8 3.5l-1.4 2c-1.2 1.6-3.4 2.2-5.3 1.4C18.8 28.7 11.3 21.2 9 15c-.8-1.9-.2-4.1 1.4-5.3z" fill="var(--white)"/>
    </svg>
    <div class="display display--bold outlined rear-phone">3907 4412</div>
    <div class="web outlined rear-web">www.brightmeadowmowing.com.au</div>

    <div class="social" style="left:443px;top:154px;width:40px;font-size:9px;">
      <span class="social-box" style="width:26px;height:26px;background:var(--social-a);"></span>Linkup
    </div>
    <div class="social" style="left:490px;top:154px;width:44px;font-size:9px;">
      <span class="social-box" style="width:26px;height:26px;background:var(--social-b);"></span>Pixgram
    </div>

    <div class="display haloed rear-tagline"><b>100%</b>&nbsp; Electric Mowing Company</div>

    <div class="services outlined centered rear-services" style="top:261px;">Mowing • Hedging • Pressure Cleaning</div>
    <div class="services outlined centered rear-services" style="top:289px;">Weed Control • Fencing • Turfing • Mulching • Rubbish Removal</div>
  </section>

  <section class="sign sign--side" aria-label="Side trailer sign">
    <div class="lawn-photo" role="img" aria-label="Photo of a freshly striped green lawn"></div>

    <span class="brand-dot" style="left:93px;top:28px;width:70px;height:70px;"></span>
    <div class="brand side-brand">BRIGHT MEADOW<br>MOWING</div>

    <div class="display outlined side-headline">Acreage &amp; Commercial Specialists</div>

    <svg class="phone-icon" style="left:251px;top:98px;" width="52" height="52" viewBox="0 0 40 40" aria-hidden="true">
      <rect x="1" y="1" width="38" height="38" rx="9" fill="var(--ink-green)" stroke="var(--white)" stroke-width="1.5"/>
      <path d="M13 9c1.5-1 3-.5 3.5.8l2 4.5c.4 1-.1 2-1 2.6l-1.6 1c1.2 2.6 3.3 4.7 5.9 5.9l1-1.6c.6-.9 1.6-1.4 2.6-1l4.5 2c1.3.5 1.8 2 .8 3.5l-1.4 2c-1.2 1.6-3.4 2.2-5.3 1.4C18.8 28.7 11.3 21.2 9 15c-.8-1.9-.2-4.1 1.4-5.3z" fill="var(--white)"/>
    </svg>
    <div class="display display--bold outlined side-phone">3907 4412</div>

    <div class="social" style="left:669px;top:98px;width:60px;font-size:11px;">
      <span class="social-box" style="width:52px;height:52px;background:var(--social-a);"></span>Linkup
    </div>
    <div class="social" style="left:740px;top:98px;width:60px;font-size:11px;">
      <span class="social-box" style="width:52px;height:52px;background:var(--social-b);"></span>Pixgram
    </div>

    <div class="web outlined side-web">www.brightmeadowmowing.com.au</div>

    <div class="display haloed side-tagline"><b>100%</b>&nbsp; Electric Mowing Company</div>
    <div class="display haloed side-est">- est 2017</div>

    <div class="services outlined centered side-services">Mowing • Hedging • Pressure Cleaning • Weed Control • Fencing • Turfing • Mulching • Rubbish Removal</div>
  </section>

</main>
</body>
</html>
```